Flyer für Logopädie, Ergo- und Physiotherapie
Zielgruppe
Logopädie, Ergotherapie, Physiotherapie, K-Vela, Fitness
Aufgabenstellung
Ich lade den alten Flyer für die Texte hoch. Dieser ist im Moment DIN lang (99 x 210 mm). Die Homepage, Flyer und die alte Praxis(wir sind umgezogen) war komplett grün gehalten. Davon sind wir abgekommen. Grün sollte es nicht mehr sein. Die Praxis ist nun mehr Braun, viel Holz, edler. Wir sind eine aktive Praxis, es soll nicht nach Wellness aussehen. Die Farben des 'Balls' aus unserem Logo soll sich nicht verändern. Ich habe Bilder vom Gebäude der Praxis hochgeladen. Falls möglichl, kann man hier unser Logo oder nur den Ball mit einfügen?
Die Adresse auf dem Flyer stimmt nicht mehr.
Lenzbacher-Weg-Str. 4
91347 Kornhain

```html
<!DOCTYPE html>
<html lang="de">
<head>
<meta charset="utf-8">
<title>Flyer Therapiepraxis – Innenseite</title>
<link href="https://fonts.googleapis.com/css2?family=Michroma&family=Barlow+Semi+Condensed:ital,wght@0,400;0,700;1,700&display=swap" rel="stylesheet">
<style>
  :root {
    --paper: #eef0f0;
    --ink: #2a2a33;
    --logo-pink: #d6338f;
    --logo-pink-soft: #e88cc0;
    --physio-blue: #3fb0e6;
    --physio-blue-soft: #a9d8f0;
    --ergo-purple: #3a2553;
    --ergo-purple-soft: #7b5f99;
    --voucher-green: #7dc142;
    --white: #ffffff;
  }
  html, body { margin: 0; padding: 0; width: 1200px; height: 900px; overflow: hidden; background: var(--paper); }
  .flyer { position: relative; width: 1200px; height: 900px; display: flex; font-family: "Barlow Semi Condensed", sans-serif; color: var(--ink); }
  .panel { position: relative; width: 400px; height: 900px; overflow: hidden; }
  .panel + .panel { border-left: 1px solid #dde0e0; }
  .panel-head { position: absolute; left: 0; top: 0; width: 400px; }
  .panel-title { position: absolute; margin: 0; font-family: "Michroma", sans-serif; font-weight: 400; font-size: 34px; color: var(--white); letter-spacing: 1px; }
  .panel-intro { position: absolute; margin: 0; font-weight: 700; font-style: italic; font-size: 14px; line-height: 1.2; text-transform: uppercase; color: var(--white); }
  .photo { position: absolute; border-radius: 50%; }
  .photo-halo { position: absolute; border-radius: 50%; }
  .service-list { position: absolute; margin: 0; padding: 0; list-style: none; font-size: 14.5px; line-height: 1.22; }
  .service-list li { position: relative; padding-left: 16px; margin-bottom: 4px; }
  .service-list li::before { content: ""; position: absolute; left: 0; top: 3px; width: 10px; height: 9px; background: var(--marker); }
  .service-list strong { display: block; font-style: italic; text-transform: uppercase; font-size: 14px; }
  .panel-logo { --marker: var(--logo-pink); }
  .panel-ergo { --marker: var(--ergo-purple-soft); }
  .offer { position: absolute; left: 60px; top: 560px; padding-left: 14px; border-left: 2px solid var(--physio-blue-soft); }
  .offer h3 { margin: 0 0 4px; font-size: 14px; font-style: italic; text-transform: uppercase; }
  .offer ul { margin: 0; padding: 0; list-style: none; font-size: 14.5px; line-height: 1.35; }
  .voucher { position: absolute; left: 190px; top: 790px; width: 230px; height: 64px; }
  .voucher p { position: absolute; left: 22px; top: 14px; margin: 0; font-weight: 700; font-style: italic; font-size: 13.5px; line-height: 1.2; color: var(--white); text-transform: uppercase; }
  .contact-bar { position: absolute; top: 14px; right: 18px; font-weight: 700; font-size: 13px; display: flex; gap: 10px; }
  .contact-bar span + span { border-left: 1.5px solid var(--ink); padding-left: 10px; }
  .ergo-note { position: absolute; right: 24px; top: 540px; margin: 0; text-align: right; font-weight: 700; font-style: italic; font-size: 14px; line-height: 1.2; text-transform: uppercase; }
</style>
</head>
<body>
<main class="flyer">

  <section class="panel panel-logo">
    <svg class="panel-head" width="400" height="330" viewBox="0 0 400 330" aria-hidden="true">
      <path d="M0 0 H400 V270 L60 300 L38 318 L18 298 L0 300 Z" fill="var(--logo-pink)"/>
    </svg>
    <h2 class="panel-title" style="left:40px;top:50px;">Logopädie</h2>
    <p class="panel-intro" style="left:40px;top:125px;width:200px;">Therapie von Stimm-, Sprech-, Sprach- und Schluckstörungen bei Kindern und Erwachsenen.</p>
    <div class="photo-halo" style="left:250px;top:160px;width:140px;height:140px;background:var(--logo-pink-soft);opacity:.8;"></div>
    <div class="photo" role="img" aria-label="Foto: Logopädin im Gespräch mit einem Kind am Tisch" style="left:210px;top:210px;width:190px;height:190px;background:radial-gradient(circle at 60% 40%, #e9e4df, #8d8580 70%, #3b3536);"></div>
    <ul class="service-list" style="left:30px;top:410px;width:330px;">
      <li><strong>Sprachentwicklungsstörung</strong>Probleme bei der Aussprache, in der Grammatik, im Wortschatz, im Sprachverständnis</li>
      <li><strong>Therapie nach Vallero</strong>z.B. Therapie für Kinder mit genetischen Syndromen oder bei Fütter-, Saug- und Essproblemen im Säuglings- und Kleinkindalter</li>
      <li><strong>Falsches/ viscerales Schluckmuster</strong>Zunge drückt gegen die Zähne</li>
      <li><strong>Dysphonie - Stimmstörung</strong>Stimme ist heiser ohne Erkältung</li>
      <li><strong>Dysphagie - Schluckstörung</strong>häufiges Verschlucken, husten beim Essen/ Trinken</li>
      <li><strong>Aphasie - nach Schlaganfall</strong>häufig Störung d. Sprache, des Sprechens, des Lesens, des Schreibens, der Wortfindung od. des Sprachverständnisses</li>
      <li><strong>Dysarthrie - Störung der Sprechmotorik</strong>Lähmung der Gesichtsmuskulatur, Probleme beim Sprechen durch Zungenlähmung</li>
    </ul>
    <div class="voucher">
      <svg width="230" height="64" viewBox="0 0 230 64" aria-hidden="true"><path d="M14 0 H230 V64 H0 Z" fill="var(--voucher-green)"/></svg>
      <p>Alle Leistungen sind auch<br>als Gutschein erhältlich.</p>
    </div>
  </section>

  <section class="panel panel-physio">
    <svg class="panel-head" width="400" height="330" viewBox="0 0 400 330" aria-hidden="true">
      <path d="M0 0 H400 V260 Q300 250 270 300 Q250 280 200 270 Q80 255 0 270 Z" fill="var(--physio-blue)"/>
    </svg>
    <h2 class="panel-title" style="left:28px;top:70px;font-size:31px;">Physiotherapie</h2>
    <p class="panel-intro" style="left:30px;top:140px;width:330px;text-align:right;">Verbesserung der Bewegungs- und Funktionsfähigkeit des menschlichen Körpers, der Muskeln, des Bewegungsapparates, der Wirbelsäule und des Gangbildes durch unterschiedliche therapeutische Maßnahmen.</p>
    <div class="offer" style="top:340px;">
      <h3>Behandlungsangebot</h3>
      <ul>
        <li>manuelle Therapie</li>
        <li>Krankengymnastik</li>
        <li>Krankengymnastik am Gerät</li>
        <li>Krankengymnastik nach Berthold für Erwachsene</li>
        <li>Kiefergelenksbehandlung (CMD)</li>
        <li>manuelle Lymphdrainage</li>
        <li>klassische Massage</li>
        <li>Bindegewebsmassage</li>
        <li>Wärmetherapie (Infrarotbestrahlung)</li>
        <li>Wärmepackung (Fango)</li>
        <li>Beckenbodentraining</li>
        <li>heiße Rolle</li>
        <li>Kälteanwendung</li>
      </ul>
    </div>
    <div class="photo-halo" style="left:120px;top:690px;width:130px;height:130px;background:var(--physio-blue-soft);"></div>
    <div class="photo" role="img" aria-label="Foto: Physiotherapeut behandelt einen Patienten auf der Liege" style="left:170px;top:700px;width:190px;height:190px;background:radial-gradient(circle at 45% 45%, #f1f1f1, #9aa0a3 65%, #2f3235);"></div>
  </section>

  <section class="panel panel-ergo">
    <div class="contact-bar"><span>T. 09131 555 20 48</span><span>www.praxis-kornhain.de</span></div>
    <svg class="panel-head" width="400" height="330" viewBox="0 0 400 330" aria-hidden="true">
      <path d="M0 45 H400 V290 L360 292 L342 308 L325 290 L0 280 Z" fill="var(--ergo-purple)"/>
    </svg>
    <h2 class="panel-title" style="left:36px;top:90px;">Ergotherapie</h2>
    <p class="panel-intro" style="left:36px;top:160px;width:340px;">Verbesserung gestörter oder verloren gegangener Fähigkeiten wie Grob- und Feinmotorik, Konzentration, Ausdauer, Koordination sowie sozialer und emotionaler Kompetenzen.</p>
    <div class="photo-halo" style="left:70px;top:370px;width:150px;height:150px;background:var(--ergo-purple-soft);"></div>
    <div class="photo" role="img" aria-label="Foto: Ergotherapeutin spielt mit einem Kind mit Bausteinen" style="left:20px;top:290px;width:190px;height:190px;background:radial-gradient(circle at 55% 45%, #f3eee8, #c9b9a8 60%, #6f6470);"></div>
    <p class="ergo-note">Wir behandeln<br>Kinder und<br>Erwachsene<br>in diesen Bereichen:</p>
    <ul class="service-list" style="left:24px;top:640px;width:360px;">
      <li><strong>Motorisch- funktionelle Behandlung</strong>aktive und passive Bewegungsstörung<br>Störung der Grob- und Feinmotorik<br>Störung der Haltung</li>
      <li><strong>Psychisch- funktionelle Behandlung</strong>Funktionsstörung der Orientierung zu Raum, Zeit und Person - des Antriebs und des Willens - des Realitätsbewusstseins und der Selbsteinschätzung</li>
      <li><strong>Sensomotorisch- perzeptive Behandlung</strong>Störung der Wahrnehmung - der Körperbewegung - der Koordination</li>
      <li><strong>Hirnleistungstraining</strong>Störung der Konzentration - des Gedächtnisses - der Handlungsplanung</li>
    </ul>
  </section>

</main>
</body>
</html>
```